Coming Soon page for a new fitness startup

We are a new startup based in Toronto, Canada working on a site and mobile app where people can register for athletic events such as running, cycling, triathlon, SUP, etc.

Participants will also be able to manage their clubs and team, and connect their fitness trackers so they have all their fitness data and friends in one place.

I like very simple designs and lots of whitespace. So no need for icons or unnecessary graphics.

I prefer having a mobile phone app instead of a hero image. No need to worry about the details within the mobile app for now, we can fill it in later. Here are some landing pages that I like.
https://pixelshelf.example/tormundlaksa/buckets/493817-Landing-Page

Attached is a wireframe that gives some sample content for each of the sections. Please do not take the wireframe too literally, it is only meant to illustrate the content that we are experimenting with and should give an idea of how much text will be on the page.

I have also attached the company logo files. The logo is not being used yet so feel free to simplify the logo if it doesn't look great with your design. For example, I'm ok with just the name "vexqari" in white if that looks better.

Target Market(s)

Ages 25 to 45. Interested in running, cycling, triathlon, SUP, etc.

Industry/Entity Type

Fitness

Coding

Coded - Design and coding required

Number of Pages Required

1 page

Requirements
Should not have
• Any photos should not contain track and field events, or people in a gym. Any photos should have people running or cycling outdoors. I know that photos can be easily swapped out but it is distracting to review a design that has the wrong photos.

```html
<!DOCTYPE html>
<html lang="en">
<head>
<meta charset="utf-8">
<title>vexqari — A New Fitness Community</title>
<link rel="stylesheet" href="https://fonts.googleapis.com/css2?family=Open+Sans:ital,wght@0,400;0,600;1,600&display=swap">
<style>
:root{
  --red:#d51f35;
  --orange:#f08c1a;
  --white:#ffffff;
  --ink:#1c1c1c;
  --grey:#5a5a5a;
  --line:#b9b9b9;
  --hero-a:#f3c6c9;
  --hero-b:#f6d9c4;
  --hero-c:#e9c2a6;
}
*{margin:0;padding:0;box-sizing:border-box}
html,body{width:1200px;height:1101px;overflow:hidden;background:var(--white)}
body{position:relative;font-family:"Open Sans",sans-serif;color:var(--ink)}
.abs{position:absolute}

.hero-photo{left:0;top:0;width:1200px;height:513px;
  background:linear-gradient(100deg,var(--hero-a) 0%,var(--hero-b) 45%,var(--hero-c) 75%,#e6d8c8 100%)}
.brand{left:137px;top:139px;display:flex;align-items:center;gap:14px}
.brand-dot{width:52px;height:52px;border-radius:50%;background:var(--red)}
.brand-name{font-size:58px;font-weight:600;color:var(--grey);line-height:1}
.tagline{left:137px;top:253px;color:var(--white);font-size:21px;letter-spacing:1.4px;line-height:26px;text-transform:uppercase}

.launch-band{left:121px;top:393px;width:954px;height:203px;border-top:3px solid var(--white);
  background:linear-gradient(90deg,var(--red) 0%,#e2452a 45%,var(--orange) 100%);
  box-shadow:0 3px 6px rgba(0,0,0,.12)}
.launch-title{left:154px;top:409px;color:var(--white);font-size:27px;line-height:31px}
.launch-copy{left:151px;top:483px;color:var(--white);font-size:14px;line-height:17px;width:380px}
.email-field{left:150px;top:544px;width:275px;height:36px;background:var(--white);color:#444;font-size:12px;padding:10px 18px}
.notify-btn{left:432px;top:544px;width:96px;height:36px;border:1px solid var(--white);background:var(--red);color:var(--white);font-size:16px;font-weight:600;text-align:center;line-height:34px}
.launch-date{left:626px;top:522px;color:var(--white);font-size:21px}
.feature-tag{top:566px;height:30px;border:1px solid var(--white);color:var(--white);font-size:12.5px;text-align:center;line-height:28px}

.phone{left:854px;top:78px;width:207px;height:428px;border-radius:30px;background:#f7f7f7;border:2px solid #dcdcdc;box-shadow:0 2px 8px rgba(0,0,0,.15)}
.phone-screen{left:865px;top:129px;width:186px;height:327px;background:#f1f1f1;border:1.5px solid #222;overflow:hidden}
.app-bar{height:40px;background:var(--white);display:flex;align-items:center;justify-content:center;font-size:10px;color:#444;border-bottom:1px solid #e5e5e5}
.app-card{background:var(--white);margin:6px 6px 0;padding:6px}
.app-card-row{display:flex;align-items:center;gap:6px;font-size:6px;color:var(--red)}
.avatar{width:18px;height:18px;border-radius:50%;background:#c9a489}
.app-photo{margin:6px 6px 0;height:80px;background:linear-gradient(120deg,#7c6a5e,#b39b86)}
.app-likes{font-size:5.5px;color:#333}
.app-nav{position:absolute;left:0;bottom:0;width:100%;height:28px;background:var(--white);border-top:1px solid #ddd}
.app-fab{position:absolute;left:78px;bottom:6px;width:30px;height:30px;border-radius:50%;background:var(--red);color:var(--white);text-align:center;line-height:28px;font-size:14px}

.event-card{left:123px;top:621px;width:472px;height:400px;border:1px solid var(--line);border-top-color:var(--orange);border-right-color:var(--orange)}
.event-title{left:155px;top:636px;font-size:20px}
.event-points{left:157px;top:682px;list-style:none;width:400px}
.event-points li{position:relative;padding-left:21px;font-size:12.5px;line-height:24px;margin-bottom:6px}
.event-points li.lg{font-size:13.5px}
.event-points li::before{content:"";position:absolute;left:0;top:8px;width:9px;height:9px;border-radius:50%;background:linear-gradient(135deg,var(--orange),var(--red))}
.event-pitch{left:154px;top:868px;font-size:19.5px;line-height:31px}
.contact-btn{left:155px;top:940px;width:123px;height:41px;background:var(--red);color:var(--white);font-size:15px;text-align:center;line-height:41px}

.member-photo{left:640px;top:631px;width:204px;height:306px;background:linear-gradient(180deg,#e9cdb9 0%,#c99b7d 55%,#3aa3d8 80%,#e3c3aa 100%);border-radius:90px 90px 0 0}
.quote-panel{left:842px;top:826px;width:358px;height:111px;background:var(--red)}
.quote-name{left:856px;top:846px;color:var(--white);font-size:16px;font-style:italic;font-weight:600}
.quote-rule{left:857px;top:871px;width:16px;height:2px;background:var(--white)}
.quote-text{left:857px;top:886px;color:var(--white);font-size:12.5px;line-height:15px;width:230px}
.slide-arrow{top:816px;width:21px;height:21px;background:var(--orange)}

.site-footer{left:0;top:1054px;width:1200px;height:47px;background:var(--red);color:var(--white);font-size:12.5px;font-weight:600}
.footer-link{top:16px}
.social-dot{top:15px;width:17px;height:17px;border-radius:50%;background:var(--white)}
.copyright{right:98px;top:17px;font-weight:400}
</style>
</head>
<body>

<div class="abs hero-photo" role="img" aria-label="Soft warm photograph of a smiling woman and friends in a bright studio"></div>
<div class="abs brand"><span class="brand-dot"></span><span class="brand-name">vexqari</span></div>
<p class="abs tagline">Connect your training, friend,<br>and events in one place.</p>

<section class="abs launch-band"></section>
<h1 class="abs launch-title" style="font-weight:400">A New Fitness Community<br>is Coming Soon</h1>
<p class="abs launch-copy">Join our email list. A referal program is coming and you'll want to be the first know.</p>
<div class="abs email-field">email address</div>
<div class="abs notify-btn">Notify me</div>
<p class="abs launch-date">Launching Spring 2018</p>
<div class="abs feature-tag" style="left:614px;width:135px">Sign up for events.</div>
<div class="abs feature-tag" style="left:758px;width:138px">Invite your friends.</div>
<div class="abs feature-tag" style="left:900px;width:138px">Connect your workouts</div>

<div class="abs phone"></div>
<svg class="abs" style="left:938px;top:86px" width="40" height="12" viewBox="0 0 40 12"><circle cx="3" cy="8" r="2.5" fill="#333"/><rect x="14" y="6" width="22" height="3" rx="1.5" fill="#333"/></svg>
<svg class="abs" style="left:941px;top:462px" width="34" height="34" viewBox="0 0 34 34"><circle cx="17" cy="17" r="15" fill="#fafafa" stroke="#555" stroke-width="1.2"/></svg>
<div class="abs phone-screen">
  <div class="app-bar">vexqari</div>
  <div class="app-card"><div class="app-card-row"><span class="avatar"></span>LOREM IPSUM</div></div>
  <div class="app-photo" role="img" aria-label="Photo of a group of athletes"></div>
  <div class="app-card"><p class="app-likes">Sam &amp; 34 like this</p>
    <div class="app-card-row" style="margin-top:6px"><span class="avatar"></span><span class="avatar"></span><span class="avatar"></span><span class="avatar"></span></div></div>
  <div class="app-card"><div class="app-card-row"><span class="avatar"></span>LOREM IPSUM</div></div>
  <div class="app-nav"></div>
  <div class="app-fab">+</div>
</div>

<div class="abs event-card"></div>
<h2 class="abs event-title" style="font-weight:400">Organizing an event ?</h2>
<ul class="abs event-points">
  <li>Attacting participants &nbsp;is hard work</li>
  <li>An online presencerequired &nbsp;effort and planning</li>
  <li class="lg">Mobile apps are costly and require a tech team</li>
  <li class="lg">Ads, landing pages, A/B testing, funnel optimization, all require expertise</li>
</ul>
<p class="abs event-pitch">Lets our team of experts take care of<br>this for you. best of all, it's no cost to yoy!</p>
<div class="abs contact-btn">Contas us</div>

<div class="abs member-photo" role="img" aria-label="Photo of a smiling athlete in a blue sports top, arms crossed"></div>
<div class="abs quote-panel"></div>
<svg class="abs slide-arrow" style="left:1042px" viewBox="0 0 21 21"><rect width="21" height="21" fill="#f08c1a"/><path d="M12.5 6 L8 10.5 L12.5 15" fill="none" stroke="#fff" stroke-width="1.3"/></svg>
<svg class="abs slide-arrow" style="left:1066px" viewBox="0 0 21 21"><rect width="21" height="21" fill="#f08c1a"/><path d="M8.5 6 L13 10.5 L8.5 15" fill="none" stroke="#fff" stroke-width="1.3"/></svg>
<p class="abs quote-name">Jean Doe</p>
<div class="abs quote-rule"></div>
<p class="abs quote-text">Lorem ipsum dolor sit amet, consectetur adipisicing elit</p>

<footer class="abs site-footer">
  <span class="abs footer-link" style="left:101px">About Us</span>
  <span class="abs footer-link" style="left:175px">Developers</span>
  <span class="abs footer-link" style="left:268px">Careers</span>
  <span class="abs footer-link" style="left:341px">Contact</span>
  <span class="abs social-dot" style="left:547px"></span>
  <span class="abs social-dot" style="left:587px"></span>
  <span class="abs social-dot" style="left:620px"></span>
  <span class="abs copyright">© 2018 vexqari Inc.</span>
</footer>

</body>
</html>
```